Tolvane Clinica Business Card Design and print

I have attached the design I require including JPEG for company logo. I would like a copy of the art work for future needs.

Double sided - the item will not change from single

250 cards with both names on Ruth Pellow and Carol Dunmore

250 cards with Ruth Pellow only

Industry/Entity Type

Business

Contact Information for Business Card

See attached layout

```html
<!DOCTYPE html>
<html lang="en">
<head>
<meta charset="utf-8">
<title>Tolvane Clinica – Business Card</title>
<link href="https://fonts.googleapis.com/css2?family=Lato:wght@300;400;700&display=swap" rel="stylesheet">
<style>
  :root {
    --backdrop: #e6e6e8;
    --brand-purple: #824c9f;
    --brand-orange: #e27a23;
    --card-white: #ffffff;
    --ink: #2b2b2b;
    --shadow: rgba(0, 0, 0, 0.16);
  }
  * { margin: 0; padding: 0; box-sizing: border-box; }
  html, body {
    width: 1200px;
    height: 800px;
    overflow: hidden;
    background: var(--backdrop);
    font-family: "Lato", sans-serif;
  }
  .canvas {
    width: 1200px;
    height: 800px;
    display: flex;
    align-items: center;
    justify-content: center;
    gap: 50px;
  }
  .card {
    width: 540px;
    height: 310px;
    border-radius: 3px;
    box-shadow: 0 10px 28px var(--shadow);
    position: relative;
  }

  /* Front side */
  .card--front {
    background: var(--brand-purple);
    color: var(--card-white);
    display: flex;
    flex-direction: column;
    align-items: center;
    justify-content: center;
    gap: 26px;
  }
  .wordmark {
    display: flex;
    align-items: center;
    gap: 14px;
    font-weight: 300;
    font-size: 38px;
    letter-spacing: 1px;
    text-transform: lowercase;
  }
  .wordmark__square {
    width: 34px;
    height: 34px;
    background: currentColor;
  }
  .card--front .website {
    font-size: 14px;
    letter-spacing: 0.4px;
    font-weight: 400;
  }

  /* Back side */
  .card--back {
    background: var(--card-white);
    display: flex;
    align-items: center;
    padding: 0 36px 0 40px;
  }
  .card--back .wordmark {
    color: var(--brand-orange);
    font-size: 26px;
    gap: 10px;
    width: 230px;
    margin-top: -60px;
  }
  .card--back .wordmark__square {
    width: 30px;
    height: 30px;
    background: var(--brand-purple);
  }
  .contacts {
    margin-left: auto;
    color: var(--ink);
    font-size: 13px;
    line-height: 1.35;
  }
  .contact { margin-bottom: 10px; }
  .contact__name {
    color: var(--brand-purple);
    font-weight: 700;
    font-size: 16px;
    margin-bottom: 1px;
  }
  .contacts .website { margin-top: 6px; }
</style>
</head>
<body>
  <main class="canvas">
    <section class="card card--front" aria-label="Card front">
      <div class="wordmark">
        <span>tolvane</span>
        <span class="wordmark__square" aria-hidden="true"></span>
        <span>clinica</span>
      </div>
      <p class="website">www.tolvaneclinica.com.au</p>
    </section>

    <section class="card card--back" aria-label="Card back">
      <div class="wordmark">
        <span class="wordmark__square" aria-hidden="true"></span>
        <span>tolvane clinica</span>
      </div>
      <div class="contacts">
        <div class="contact">
          <p class="contact__name">Ruth Pellow</p>
          <p class="contact__email">ruth@tolvaneclinica.com.au</p>
          <p class="contact__phone">+61 (0)400 555 018</p>
        </div>
        <div class="contact">
          <p class="contact__name">Carol Dunmore</p>
          <p class="contact__email">carol@tolvaneclinica.com.au</p>
          <p class="contact__phone">+61 (0)400 555 027</p>
        </div>
        <p class="website">www.tolvaneclinica.com.au</p>
      </div>
    </section>
  </main>
</body>
</html>
```